Tranquil Pathway Business Card

Logo attached. (will be printing onto thick white/off white textured card)

Double sided business card for two Therapists working at Tranquil Pathway.

Require one design, but with different name and mobile numbers on each card.

Target Market(s)

Medical, Health

Industry/Entity Type

Business

Contact Information for Business Card

Need one business card design, but a separate card for each person - Colin Marchetti and Marieke de Boeckx.

FRONT OF CARD

Logo

Name (Colin Marchetti on one card, Marieke de Boeckx on the other)
Professional Clinical Hypnotherapist

Consulting Rooms (Near Lindqvist Hospital)
482 Brackenfield Road
Dunmore VIC 3987

Colin@TranquilPathway.example.au OR Marieke@TranquilPathway.example.au

Mobile: 0455 872 604 (for Colin) OR
Mobile: 0467 290 518 (for Marieke)

BACK OF CARD

Logo

Website: www.TranquilPathway.example.au

Phone: 1300 958 471

Requirements
Must have
• Text and logo only. No additiional graphics.

```html
<!DOCTYPE html>
<html lang="en">
<head>
<meta charset="utf-8">
<title>Tranquil Pathway Business Card</title>
<link href="https://fonts.googleapis.com/css2?family=Open+Sans:wght@400;600;700&display=swap" rel="stylesheet">
<style>
  :root {
    --backdrop: #a3a3a3;
    --card: #fbfbfa;
    --navy: #1f2a66;
    --ink: #2b2b2f;
    --rule: #9a9a9a;
    --ring: #5e5f63;
  }
  * { margin: 0; padding: 0; box-sizing: border-box; }
  html, body { width: 1200px; height: 1200px; overflow: hidden; }
  body {
    background: var(--backdrop);
    font-family: "Open Sans", Arial, sans-serif;
    color: var(--ink);
    position: relative;
  }
  .card {
    position: absolute;
    left: 190px;
    width: 820px;
    height: 500px;
    background: var(--card);
    box-shadow: 0 4px 14px rgba(0,0,0,0.18);
  }
  .card--back { top: 75px; }
  .card--front { top: 625px; }

  .brand {
    display: flex;
    align-items: center;
    gap: 16px;
    position: absolute;
  }
  .brand__dot {
    width: 72px; height: 72px;
    border-radius: 50%;
    background: var(--navy);
    border: 6px solid var(--ring);
  }
  .brand__name {
    font-weight: 700;
    font-size: 30px;
    color: var(--navy);
    letter-spacing: 0.5px;
    padding-left: 16px;
    border-left: 1px solid var(--rule);
    line-height: 80px;
  }

  .card--back .brand { left: 50%; top: 170px; transform: translateX(-50%); }
  .back-contact {
    position: absolute;
    left: 0; right: 0; bottom: 50px;
    text-align: center;
    font-size: 18px;
    line-height: 1.45;
  }

  .card--front .brand { left: 60px; top: 150px; }
  .brand--small .brand__dot { width: 60px; height: 60px; border-width: 5px; }
  .brand--small .brand__name { font-size: 25px; line-height: 66px; padding-left: 12px; }

  .details {
    position: absolute;
    right: 55px;
    top: 120px;
    text-align: right;
  }
  .details__name {
    font-weight: 700;
    font-size: 27px;
    color: var(--navy);
    line-height: 1.15;
  }
  .details__role {
    font-weight: 600;
    font-size: 17px;
    margin-bottom: 34px;
  }
  .details__lines {
    font-size: 18px;
    line-height: 1.45;
  }
</style>
</head>
<body>
  <section class="card card--back" aria-label="Card back">
    <div class="brand">
      <div class="brand__dot"></div>
      <div class="brand__name">TRANQUIL PATHWAY</div>
    </div>
    <div class="back-contact">
      <p>Colin@TranquilPathway.example.au</p>
      <p>Mobile: 0455 872 604</p>
    </div>
  </section>

  <section class="card card--front" aria-label="Card front">
    <div class="brand brand--small">
      <div class="brand__dot"></div>
      <div class="brand__name">TRANQUIL PATHWAY</div>
    </div>
    <div class="details">
      <p class="details__name">Colin Marchetti</p>
      <p class="details__role">Professional Clinical Hypnotherapist</p>
      <div class="details__lines">
        <p>Consulting Rooms (Near Lindqvist Hospital)</p>
        <p>482 Brackenfield Road</p>
        <p>Dunmore VIC 3987</p>
        <p>Colin@TranquilPathway.example.au</p>
        <p>Mobile: 0455 872 604</p>
      </div>
    </div>
  </section>
</body>
</html>
```